Security Guard company needs new procedure template to wow potential clients in tender submissions

We need an update to our procedure template that will look very professional and modern. We have many procedures so this template must be editable so the content can be adjusted by us depending on the procedure.
A smart and modern professional front page with editable title etc.
A professional and modern page template for the body of the procedure.

We wish to copy and paste our word document onto this template and be able to use it easily.

I have attached our logo and example of a procedure we have.

Font styles to use
Sans Serif

Requirements
Must have
• Ability for me to edit text and add new sections to the document.
Use as a template for multiple procedures.

```html
<!DOCTYPE html>
<html lang="en">
<head>
<meta charset="utf-8">
<title>Northgate Guarding – HSE Policy Template</title>
<link href="https://fonts.googleapis.com/css2?family=Poppins:wght@400;500;600;700;800;900&display=swap" rel="stylesheet">
<style>
:root{
  --red:#e31e25;
  --red-dark:#b8141a;
  --black:#111111;
  --ink:#2a2a2a;
  --paper:#ffffff;
  --paper-shade:#ececec;
  --stage:#b3b3b3;
  --white:#ffffff;
}
*{box-sizing:border-box;margin:0;padding:0}
html,body{width:1200px;height:3494px;overflow:hidden}
body{background:var(--stage);font-family:'Poppins',sans-serif;color:var(--ink);position:relative}

.sheet{position:absolute;background:linear-gradient(160deg,var(--paper) 0%,var(--paper) 55%,var(--paper-shade) 100%);box-shadow:0 4px 10px rgba(0,0,0,.25);overflow:hidden}

/* cover */
.cover{left:327px;top:176px;width:564px;height:800px;border-top:7px solid var(--red)}
.cover-brand{position:absolute;left:0;right:0;top:78px;display:flex;align-items:center;justify-content:center;gap:14px}
.brand-square{width:30px;height:30px;background:var(--red)}
.brand-name{font-weight:600;color:var(--red);font-size:38px;line-height:1}
.cover-shield{position:absolute;left:87px;top:165px;width:393px;height:420px}
.cover-kicker{position:absolute;left:0;right:0;top:580px;text-align:center;font-weight:800;font-size:29px;color:var(--black);letter-spacing:-.3px}
.cover-title{position:absolute;left:0;right:0;top:610px;text-align:center;font-weight:900;font-size:128px;line-height:1;color:var(--red);letter-spacing:-2px}
.cover-bar{position:absolute;left:0;right:0;top:740px;height:30px;background:var(--black);color:var(--white);font-size:13px;letter-spacing:1.2px;display:flex;align-items:center;padding-left:40px}
.cover-bar .sep{margin:0 16px}

/* inner pages */
.page{width:522px;height:736px}
.page-head{position:absolute;left:0;top:0;right:0;height:58px;background:linear-gradient(90deg,var(--red) 0%,var(--red-dark) 100%);display:flex;align-items:center;justify-content:space-between;padding:0 30px 0 36px}
.page-title{color:var(--white);font-weight:700;font-size:16px;position:relative}
.page-title::after{content:"";position:absolute;left:0;bottom:-7px;width:48px;height:2px;background:var(--white)}
.head-brand{display:flex;align-items:center;gap:6px;color:var(--white)}
.head-brand .mark{width:12px;height:12px;background:var(--white)}
.head-brand .nm{font-weight:600;font-size:13px;line-height:1}
.page-foot{position:absolute;left:36px;right:36px;bottom:10px;display:flex;justify-content:space-between;align-items:center;font-size:6.5px;font-weight:600;color:var(--ink)}
.page-num{width:13px;height:14px;border:1.3px solid var(--red);border-radius:2px 2px 6px 6px;font-size:6.5px;display:flex;align-items:center;justify-content:center}

.toc{position:absolute;left:68px;top:95px;width:400px;list-style:none}
.toc li{display:flex;height:35px;align-items:center;font-size:10.5px}
.toc .name{width:200px}
.toc .dots{width:185px;border-top:1.5px dashed #333;height:0;margin-right:40px}

.photo{position:absolute}
.dark-box{position:absolute;background:var(--black);color:var(--white);padding:40px 22px 0 20px}
.sec-head{font-weight:700;color:var(--red);font-size:19px;line-height:1.2;margin-bottom:8px}
.dark-box p,.dark-box li{font-size:10px;line-height:1.3}
.bullets{list-style:none}
.bullets li{position:relative;padding-left:16px;margin-top:8px}
.bullets li::before{content:"";position:absolute;left:0;top:3px;width:7px;height:7px;border:2px solid var(--red);border-radius:50%}

.body-text{position:absolute;left:36px;right:36px;top:82px}
.body-text .role{font-weight:700;color:var(--red);font-size:17px;display:inline-block;border-bottom:2px solid var(--red);line-height:1.15;margin-bottom:7px}
.body-text p,.body-text li{font-size:10px;line-height:1.25;text-align:justify}
.body-text .bullets li{margin-top:12px}
.body-text .role.next{margin-top:18px}
</style>
</head>
<body>

<!-- Cover -->
<section class="sheet cover">
  <div class="cover-brand">
    <div class="brand-square"></div>
    <div class="brand-name">Northgate Guarding</div>
  </div>
  <svg class="cover-shield" viewBox="0 0 393 420" role="img" aria-label="Photo of hands typing on a laptop beside a coffee mug, framed in a shield">
    <defs>
      <linearGradient id="photoTone" x1="0" y1="0" x2="1" y2="1">
        <stop offset="0" stop-color="#7a4a32"/>
        <stop offset=".5" stop-color="#b7aca6"/>
        <stop offset="1" stop-color="#5c4030"/>
      </linearGradient>
    </defs>
    <path d="M0 0 H393 V210 C393 320 300 380 196 420 C93 380 0 320 0 210 Z" fill="var(--black)"/>
    <path d="M14 12 H379 V210 C379 312 292 366 196 404 C101 366 14 312 14 210 Z" fill="var(--red)"/>
    <path d="M28 24 H365 V210 C365 302 285 352 196 388 C108 352 28 302 28 210 Z" fill="var(--white)"/>
    <path d="M38 34 H355 V210 C355 296 280 342 196 376 C113 342 38 296 38 210 Z" fill="url(#photoTone)"/>
  </svg>
  <div class="cover-kicker">HEALTH, SAFETY &amp; ENVIRONMENT</div>
  <div class="cover-title">POLICY</div>
  <div class="cover-bar">NGL- HSE001 – Health, Safety and Environment Policy<span class="sep">|</span>Rev 2</div>
</section>

<!-- Table of contents -->
<section class="sheet page" style="left:61px;top:1176px">
  <header class="page-head">
    <h2 class="page-title">TABLE OF CONTENTS</h2>
    <div class="head-brand"><span class="mark"></span><span class="nm">Northgate Guarding</span></div>
  </header>
  <ul class="toc">
    <li><span class="name">Purpose</span><span class="dots"></span>3</li>
    <li><span class="name">Scope</span><span class="dots"></span>3</li>
    <li><span class="name">Responsibilities</span><span class="dots"></span>4</li>
    <li><span class="name">HSE Management System</span><span class="dots"></span>7</li>
    <li><span class="name">NGL HSE Core Values</span><span class="dots"></span>8</li>
    <li><span class="name">NGL HSE Policy Statement</span><span class="dots"></span>8</li>
    <li><span class="name">NGL HSE Policy Commitments</span><span class="dots"></span>9</li>
    <li><span class="name">Accidents</span><span class="dots"></span>10</li>
    <li><span class="name">Consultation</span><span class="dots"></span>11</li>
    <li><span class="name">Fire</span><span class="dots"></span>12</li>
    <li><span class="name">Personal Protective Equipment</span><span class="dots"></span>13</li>
    <li><span class="name">Housekeeping</span><span class="dots"></span>14</li>
    <li><span class="name">Waste Disposal</span><span class="dots"></span>15</li>
    <li><span class="name">Monitoring</span><span class="dots"></span>16</li>
    <li><span class="name">Training</span><span class="dots"></span>17</li>
    <li><span class="name">Fit to Work Policy</span><span class="dots"></span>18</li>
    <li><span class="name">Drug and Alcohol Policy</span><span class="dots"></span>19</li>
  </ul>
  <footer class="page-foot"><span>NGL- HSE001 – Health, Safety and Environment Policy &nbsp;|&nbsp; Rev 2</span><span class="page-num">2</span></footer>
</section>

<!-- Purpose & scope -->
<section class="sheet page" style="left:610px;top:1176px">
  <header class="page-head">
    <span></span>
    <div class="head-brand"><span class="mark"></span><span class="nm">Northgate Guarding</span></div>
  </header>
  <div class="photo" role="img" aria-label="Photo of a person writing in a notebook at a desk" style="left:0;top:66px;width:380px;height:626px;background:linear-gradient(160deg,#8d8d8d 0%,#d9d9d9 45%,#6b6b6b 100%)"></div>
  <div class="dark-box" style="left:187px;top:175px;width:335px;height:387px">
    <h3 class="sec-head">PURPOSE</h3>
    <p>The purpose of this Health and Safety (HSE) Plan is to:</p>
    <ul class="bullets">
      <li>Provide a statement of the Northgate Guarding Limited (NGL) aspired level of Health and Safety performance and how this will be reached over the current year.</li>
      <li>Document the Health &amp; Safety objectives, targets, key performance indicators, improvement plans, audits and communication initiatives.</li>
    </ul>
    <h3 class="sec-head" style="margin-top:24px">SCOPE</h3>
    <p style="text-align:justify">This annual Health and Safety plan is issued as a part of the NGL Health and Safety Management System. This plan covers all activities undertaken by NGL.</p>
  </div>
  <footer class="page-foot"><span>NGL- HSE001 – Health, Safety and Environment Policy &nbsp;|&nbsp; Rev 2</span><span class="page-num">3</span></footer>
</section>

<!-- Owner & custodian -->
<section class="sheet page" style="left:61px;top:1942px">
  <header class="page-head">
    <h2 class="page-title">RESPONSIBILITIES</h2>
    <div class="head-brand"><span class="mark"></span><span class="nm">Northgate Guarding</span></div>
  </header>
  <div class="body-text">
    <h3 class="role">OWNER</h3>
    <p>The Owner of this HSE Plan is the Director, who has the collective responsibility for :</p>
    <ul class="bullets">
      <li>Approving and endorsing the HSE Plan.</li>
      <li>Ensuring that resources are available to execute the HSE Plan</li>
      <li>Monitoring implementation of the HSE Plan and initiating corrective action where necessary.</li>
    </ul>
    <h3 class="role next">CUSTODIAN</h3>
    <p>The Custodian of the plan is the Operations Manager who has the responsibility for :</p>
    <ul class="bullets">
      <li>Developing the plan.</li>
      <li>Reporting status of implementation of the HSE Plan and the need for adjustments.</li>
      <li>Ensuring that employees are competent and adequately trained to discharge their defined HSE responsibilities.</li>
      <li>Ensuring employees under their control discharge their defined HSE responsibilities.</li>
      <li>Ensuring that they, and all employees under their direction, adhere to the HSE policy and procedure.</li>
    </ul>
  </div>
  <div class="photo" role="img" aria-label="Photo of a laptop with code on screen, a phone and a notebook on a white desk" style="left:0;top:445px;width:522px;height:259px;background:linear-gradient(180deg,rgba(255,255,255,0) 0%,#d6d6d6 35%,#9a9a9a 100%)"></div>
  <footer class="page-foot"><span>NGL- HSE001 – Health, Safety and Environment Policy &nbsp;|&nbsp; Rev 2</span><span class="page-num">4</span></footer>
</section>

<!-- Implementer -->
<section class="sheet page" style="left:613px;top:1942px">
  <header class="page-head">
    <h2 class="page-title">RESPONSIBILITIES</h2>
    <div class="head-brand"><span class="mark"></span><span class="nm">Northgate Guarding</span></div>
  </header>
  <div class="body-text">
    <h3 class="role">IMPLEMENTER</h3>
    <p>The Implementers of the plan are the Supervisors who have the responsibility for :</p>
    <ul class="bullets">
      <li>Carrying out pre contract site health, safety and welfare assessments;</li>
      <li>Ensuring risk assessments, welfare arrangements and emergency procedures are defined in assignment instructions;</li>
      <li>Ensuring employees are provided with information, training and supervision as necessary to work safely;</li>
      <li>Undertaking site inspections to ensure assignment instructions are being adhered to;</li>
      <li>Consulting with Security Officers on safety matters;</li>
      <li>Undertaking accident investigations of all incidents with the potential for serious injury;</li>
      <li>Ensuring that they and all employees under their direction adhere to the safety policy and procedures;</li>
      <li>Reporting to the Operations Manager any areas where the effectiveness of the safety policy and procedures could be improved.</li>
    </ul>
  </div>
  <div class="photo" role="img" aria-label="Black and white photo of chess pieces on a chessboard" style="left:0;top:445px;width:522px;height:259px;background:linear-gradient(180deg,rgba(255,255,255,0) 0%,#bdbdbd 40%,#2e2e2e 100%)"></div>
  <footer class="page-foot"><span>NGL- HSE001 – Health, Safety and Environment Policy &nbsp;|&nbsp; Rev 2</span><span class="page-num">5</span></footer>
</section>

<!-- All employees -->
<section class="sheet page" style="left:339px;top:2705px">
  <header class="page-head">
    <h2 class="page-title">RESPONSIBILITIES</h2>
    <div class="head-brand"><span class="mark"></span><span class="nm">Northgate Guarding</span></div>
  </header>
  <div class="photo" role="img" aria-label="Photo of hands holding a phone above a calendar on a wooden table" style="left:0;top:66px;width:390px;height:631px;background:linear-gradient(170deg,#3a3a36 0%,#7a6a60 45%,#c9c4bf 62%,#4a3328 100%)"></div>
  <div class="dark-box" style="left:187px;top:176px;width:335px;height:384px;padding-top:54px">
    <h3 class="sec-head" style="font-size:17px">ALL NGL EMPLOYEES</h3>
    <p>All Employees are responsible for :</p>
    <ul class="bullets">
      <li>Co-operating in health and safety inspections, risk assessments and accident investigations as required;</li>
      <li>Attending training courses as and when required;</li>
      <li>Following the HSE procedures;</li>
      <li>Undertaking their work in a safe manner in accordance with instructions and training provided;</li>
      <li>Reporting any unsafe occurrences by notifying their Supervisor/ Operations Manager as appropriate.</li>
    </ul>
  </div>
  <footer class="page-foot"><span>NGL- HSE001 – Health, Safety and Environment Policy &nbsp;|&nbsp; Rev 2</span><span class="page-num">6</span></footer>
</section>

</body>
</html>
```